Successfully Managing through a Hurricane Training Event

This learning event is specifically for Birch Supply retailers/stores located outside of the US who are seeking guidance and help with how to plan, prepare, manage there business during Hurricane/Tropical Storm season.

----------------------------------------------
Event Title: Successfully Managing Through Hurricane Season

Event Description: Hurricanes and severe tropical storms are some of the most devastating, and costly, natural disasters known to humans. In fact, historically, 40% of small businesses impacted by a natural disaster do not reopen. If your business is vulnerable to these potential catastrophic events, it is important to develop an effective preparedness and mitigation plan, and take prompt action. Doing so will not only increase the safety of your store associates and customers, but it will help you remain in business after a hurricane strikes, improving your community’s ability to recover. This session focuses on:

o In-store preparation functions
o Implementing business continuity operating procedures for protecting and maintaining your business
o Sustaining the capability to provide products to customers
o Building a hurricane-ready optimized assortment of in-demand products, including special merchandising opportunities
o Deploying effective inventory management and system strategies for staying in stock
o Knowing your available contacts and rules of engagement
o Preserving a competitive advantage and reputation
o Optimizing the means by which you leverage your freight forwarding facility

Event is hosted by: Birch Worldwide Partners www.birchworldpartnersco.example

Logistical Details:
• Length: 1 hour
• Date: Friday, August 17, 2018
• Time: 1:00 – 2:00 p.m.

To Register for this Event, Go To: https://www.tolvenork.example/birch18/fall/

Pricing: $ 25 per participant
*Charged to Invoice post-show

Questions? For more information, contact Martin Oakes
+1 555-017-2846
moakes@birchsupply.example

Target Market(s)

Birch Supply International Stores

Industry/Entity Type

Retail

Font styles to use
Serif

Requirements
Must have
• See Word File Attachment
• Use Birch Supply red and black logo colors.
• 1 -Sided brochure
Nice to have
Should not have
• N/A

```html
<!DOCTYPE html>
<html lang="en">
<head>
<meta charset="utf-8">
<title>Successfully Managing Through Hurricane Season</title>
<link href="https://fonts.googleapis.com/css2?family=Montserrat:wght@300;400;700;800&family=Open+Sans:wght@400;600;700&family=Oswald:wght@500;700&family=Roboto+Condensed:wght@400;700&display=swap" rel="stylesheet">
<style>
  :root {
    --red: #d71f26;
    --red-dark: #a3151b;
    --ink: #231f20;
    --panel-dark: #2a2a2c;
    --panel-grey: #e2e2e2;
    --paper: #ffffff;
    --text: #333333;
  }
  * { box-sizing: border-box; margin: 0; padding: 0; }
  html, body { width: 800px; height: 1200px; overflow: hidden; background: var(--paper); }
  .flyer { position: relative; width: 800px; height: 1200px; overflow: hidden; background: var(--paper); font-family: "Open Sans", sans-serif; color: var(--text); }
  .abs { position: absolute; }

  .brand { left: 44px; top: 34px; display: flex; align-items: center; gap: 12px; }
  .brand-dot { width: 50px; height: 50px; border-radius: 50%; background: var(--red); }
  .brand-name { font-family: "Montserrat", sans-serif; font-weight: 800; font-size: 24px; color: var(--ink); letter-spacing: -0.3px; }

  .header-lines { left: 0; top: 0; width: 800px; height: 140px; }

  .hero-photo { left: 0; top: 135px; width: 800px; height: 300px;
    background: linear-gradient(180deg, #9fb0bd 0%, #7d8f9a 35%, #4f6266 62%, #8a9ea4 80%, #5b6d70 100%); }

  .title-block { left: 0; top: 420px; width: 428px; height: 192px; background: var(--red); color: #fff; text-align: center; padding-top: 26px; }
  .title-block::after { content: ""; position: absolute; left: 0; bottom: 0; width: 100%; height: 62px; background: var(--red-dark); z-index: 0; }
  .title-block span { position: relative; z-index: 1; display: block; font-family: "Montserrat", sans-serif; }
  .title-main { font-weight: 800; font-size: 40px; line-height: 1.05; }
  .title-sub { font-weight: 300; font-size: 40px; letter-spacing: 5px; line-height: 1.1; }
  .title-tail { font-weight: 700; font-size: 21px; margin-top: 12px; }

  .desc { left: 444px; top: 478px; width: 340px; }
  .desc h2 { font-family: "Roboto Condensed", sans-serif; font-weight: 700; color: var(--red); font-size: 24px; margin-bottom: 8px; }
  .desc p { font-size: 11px; line-height: 14px; }

  .topics { left: 444px; top: 676px; width: 356px; background: var(--panel-dark); color: #fff; padding: 14px 18px 8px 22px; list-style: none; }
  .topics li { position: relative; padding-left: 16px; font-size: 12px; line-height: 14.5px; margin-bottom: 7px; }
  .topics li::before { content: ""; position: absolute; left: 0; top: 5px; width: 5px; height: 5px; background: #fff; }

  .host { left: 30px; top: 654px; width: 400px; }
  .host h3 { font-family: "Roboto Condensed", sans-serif; font-weight: 700; color: var(--red); font-size: 28px; margin-bottom: 4px; }
  .host p { font-size: 20px; line-height: 26px; color: var(--ink); font-weight: 600; }

  .logistics { left: 12px; top: 768px; width: 405px; height: 160px; background: var(--panel-grey); text-align: center; padding-top: 14px; font-family: "Roboto Condensed", sans-serif; color: var(--ink); }
  .logistics h3 { font-size: 26px; font-weight: 700; margin-bottom: 4px; }
  .logistics p { font-size: 19px; line-height: 25px; }
  .logistics .label { color: var(--red); }

  .register { left: 12px; top: 934px; width: 405px; text-align: center; }
  .register-note { font-family: "Roboto Condensed", sans-serif; font-weight: 700; font-size: 18px; color: var(--ink); margin-bottom: 6px; }
  .register-link { background: var(--red-dark); color: #fff; border-radius: 22px; font-family: "Roboto Condensed", sans-serif; font-weight: 700; font-size: 19px; padding: 8px 0; }

  .price { left: 70px; top: 1010px; display: flex; align-items: center; gap: 10px; font-family: "Oswald", sans-serif; }
  .price-amount { color: var(--red); font-weight: 700; font-size: 90px; line-height: 1; }
  .price-unit { color: var(--ink); line-height: 1; }
  .price-per { font-size: 26px; font-weight: 500; display: block; }
  .price-who { font-size: 34px; font-weight: 700; display: block; }
  .price-note { font-family: "Open Sans", sans-serif; font-size: 10px; display: block; margin-top: 6px; }

  .contact { left: 470px; top: 1008px; width: 320px; font-family: "Roboto Condensed", sans-serif; color: var(--ink); }
  .contact-lead { font-size: 20px; font-weight: 700; }
  .contact-name { font-size: 30px; font-weight: 700; color: var(--red); margin: 4px 0 10px; }
  .contact-row { display: flex; align-items: center; gap: 12px; font-size: 15px; margin-bottom: 10px; font-weight: 700; }
  .contact-row svg { width: 16px; height: 16px; fill: var(--red); }

  .footer-bands { left: 0; top: 1140px; width: 800px; height: 60px; }
</style>
</head>
<body>
<main class="flyer">
  <svg class="abs header-lines" viewBox="0 0 800 140">
    <polyline points="0,128 430,128 480,96 800,96" fill="none" stroke="#d71f26" stroke-width="3"/>
    <polyline points="460,128 500,104 800,104" fill="none" stroke="#d71f26" stroke-width="2"/>
  </svg>

  <div class="abs brand">
    <span class="brand-dot"></span>
    <span class="brand-name">BIRCH WORLDWIDE PARTNERS</span>
  </div>

  <div class="abs hero-photo" role="img" aria-label="Hurricane winds bending a palm tree as storm waves crash against a seaside house"></div>

  <h1 class="abs title-block">
    <span class="title-main">SUCCESSFULLY</span>
    <span class="title-sub">MANAGING</span>
    <span class="title-tail">THROUGH HURRICANE SEASON</span>
  </h1>

  <section class="abs desc">
    <h2>Event Description:</h2>
    <p>Hurricanes and severe tropical storms are some of the most devastating, and costly, natural disasters known to humans. In fact, historically, 40% of small businesses impacted by a natural disaster do not reopen. If your business is vulnerable to these potential catastrophic events, it is important to develop an effective preparedness and mitigation plan, and take prompt action. Doing so will not only increase the safety of your store associates and customers, but it will help you remain in business after a hurricane strikes, improving your community’s ability to recover. This session focuses on:</p>
  </section>

  <ul class="abs topics">
    <li>In-store preparation functions</li>
    <li>Implementing business continuity operating procedures for protecting and maintaining your business</li>
    <li>Sustaining the capability to provide products to customers</li>
    <li>Building a hurricane-ready optimized assortment of in-demand products, including special merchandising opportunities</li>
    <li>Deploying effective inventory management and system strategies for staying in stock</li>
    <li>Knowing your available contacts and rules of engagement</li>
    <li>Preserving a competitive advantage and reputation</li>
    <li>Optimizing the means by which you leverage your freight forwarding facility</li>
  </ul>

  <section class="abs host">
    <h3>EVENT IS HOSTED BY:</h3>
    <p>Birch Worldwide Partners</p>
    <p>www.birchworldpartnersco.example</p>
  </section>

  <section class="abs logistics">
    <h3>LOGISTICAL DETAILS:</h3>
    <p>LENGTH: 1 HOUR</p>
    <p><span class="label">DATE:</span> Friday, August 17, 2018</p>
    <p><span class="label">TIME:</span> 1:00 – 2:00 p.m.</p>
  </section>

  <section class="abs register">
    <p class="register-note">TO REGISTER FOR THIS EVENT, GO TO:</p>
    <p class="register-link">https://www.tolvenork.example/birch18/fall/</p>
  </section>

  <div class="abs price">
    <span class="price-amount">$25</span>
    <span class="price-unit">
      <span class="price-per">PER</span>
      <span class="price-who">PARTICIPANT</span>
      <span class="price-note">*Charged to Invoice post-show</span>
    </span>
  </div>

  <section class="abs contact">
    <p class="contact-lead">For more information, contact</p>
    <p class="contact-name">MARTIN OAKES</p>
    <p class="contact-row">
      <svg viewBox="0 0 24 24"><path d="M6.6 10.8a15 15 0 0 0 6.6 6.6l2.2-2.2a1 1 0 0 1 1-.25 11.4 11.4 0 0 0 3.6.57 1 1 0 0 1 1 1V20a1 1 0 0 1-1 1A17 17 0 0 1 3 4a1 1 0 0 1 1-1h3.5a1 1 0 0 1 1 1c0 1.25.2 2.45.57 3.57a1 1 0 0 1-.25 1z"/></svg>
      +1 555-017-2846
    </p>
    <p class="contact-row">
      <svg viewBox="0 0 24 24"><path d="M2 5h20v14H2z M2 5l10 8 10-8" fill="none" stroke="#d71f26" stroke-width="2.4"/></svg>
      moakes@birchsupply.example
    </p>
  </section>

  <svg class="abs footer-bands" viewBox="0 0 800 60">
    <polygon points="0,8 420,8 470,60 0,60" fill="#231f20"/>
    <polygon points="420,20 800,20 800,32 432,32" fill="#d71f26"/>
    <polygon points="436,38 800,38 800,60 456,60" fill="#231f20"/>
  </svg>
</main>
</body>
</html>
```